Financial Advisor Brochure to attract new clients

I am launching a new career as a Financial Advisor and a flier that shows what services I offer and why I decided to go back to work at this point in my life. I have a deep desire to help people meet their dreams and believe that a solid financial foundation provides the ability to live your life as you want to and not how you have to. I created a simple flier but know that so much more can be done to catch a persons eye.

Target Market(s)

Entrepeneurs and Woman in all stages of life.

Industry/Entity Type

Financial Advisor

Font styles to use
Sans Serif

Colors
00AB8E
00BBA5
67D7C9
C6EFE9
E9F9F6

Requirements
Must have
• my photo, contact information and Cobaltra Logo

```html
<!DOCTYPE html>
<html lang="en">
<head>
<meta charset="utf-8">
<title>Carla Vandermeer – Financial Advisor</title>
<link href="https://fonts.googleapis.com/css2?family=Montserrat:wght@400;500;600;700;800&family=Great+Vibes&display=swap" rel="stylesheet">
<style>
  :root{
    --forest:#2f5b1e;
    --forest-deep:#2a5219;
    --lime:#b4e86a;
    --lime-soft:#8cc65a;
    --cream:#f4fce9;
    --mint:#e9f7d4;
    --ink:#1f2a1a;
    --white:#ffffff;
  }
  *{box-sizing:border-box;margin:0;padding:0}
  html,body{width:804px;height:1200px;overflow:hidden;background:var(--white)}
  body{font-family:'Montserrat',sans-serif;color:var(--ink)}
  .flyer{position:relative;width:804px;height:1200px;background:var(--white);overflow:hidden}

  /* left column */
  .left-bg{position:absolute;left:0;top:12px;width:432px;height:1124px;background:var(--cream)}
  .left-diag{position:absolute;left:0;top:12px}
  .green-block{position:absolute;left:0;top:12px;width:404px;height:451px;background:var(--forest)}
  .photo{position:absolute;left:32px;top:53px;width:340px;height:510px;border-radius:170px 170px 0 0;
    background:linear-gradient(180deg,#d9d9d9 0%,#e6e6e6 45%,#1a9a7e 75%,#158a70 100%)}
  .name{position:absolute;left:0;width:404px;top:588px;text-align:center;font-family:'Great Vibes',cursive;
    font-size:50px;color:var(--forest);line-height:1}
  .title{position:absolute;left:0;width:404px;top:652px;text-align:center;font-size:21px;font-weight:500;color:var(--ink)}
  .title-rule{position:absolute;left:65px;top:700px;width:274px;height:3px;
    background:linear-gradient(90deg,var(--forest) 0 46%,var(--lime-soft) 46% 100%)}
  .profile{position:absolute;left:33px;top:732px;width:350px}
  .profile h2{font-size:16px;font-weight:700;color:var(--forest);margin-bottom:14px}
  .profile p{font-size:13.6px;font-weight:500;line-height:21px}
  .story{position:absolute;left:0;top:864px;width:404px;height:272px;background:var(--mint);padding:26px 8px 0 30px}
  .story p{font-size:13.5px;font-weight:500;line-height:19.6px;margin-bottom:19px}

  /* right column */
  .top-rule{position:absolute;left:432px;top:12px;width:372px;height:8px;background:var(--forest)}
  .about{position:absolute;left:432px;top:20px;width:372px;height:400px;background:var(--cream);overflow:hidden}
  .about-shade{position:absolute;left:0;top:0}
  .about-text{position:relative;padding:20px 40px 0 14px}
  .about-text p{font-size:13.6px;font-weight:500;line-height:19.6px;margin-bottom:20px}

  .services{position:absolute;left:432px;top:420px;width:372px;height:716px;background:var(--forest);color:var(--white);padding:20px 56px 0 12px}
  .services h2{font-size:17px;font-weight:700;margin-bottom:16px;white-space:nowrap}
  .svc{margin-bottom:20px}
  .svc h3{font-size:14.5px;font-weight:500;color:var(--lime);margin:0 0 9px 12px;display:flex;align-items:center;gap:8px}
  .svc h3::before{content:"";width:4px;height:4px;border-radius:50%;background:var(--white)}
  .svc ul{list-style:none}
  .svc li{font-size:14px;line-height:19.6px;padding-left:26px;position:relative}
  .svc li svg{position:absolute;left:10px;top:5px}
  .cta{font-size:14px;font-weight:700;color:var(--lime);margin:24px 0 14px 26px;letter-spacing:.2px;white-space:nowrap}
  .phone{display:flex;align-items:center;margin-left:26px;width:210px;height:32px;border-radius:16px;background:var(--lime);
    font-size:20px;font-weight:800;color:var(--forest)}
  .phone-icon{width:28px;height:28px;border-radius:50%;background:var(--white);margin:0 14px 0 2px;display:flex;align-items:center;justify-content:center}
  .web{display:flex;align-items:center;gap:14px;margin:12px 0 0 36px;font-size:14.5px;font-weight:500;white-space:nowrap}
  .web b{font-weight:700;color:var(--lime)}

  .footer{position:absolute;left:0;top:1151px;width:804px;height:36px;background:var(--forest-deep);color:var(--white);
    display:flex;align-items:center;justify-content:center;gap:8px;font-size:14px;font-weight:600}
</style>
</head>
<body>
<div class="flyer">
  <div class="left-bg"></div>
  <svg class="left-diag" width="432" height="460" viewBox="0 0 432 460" aria-hidden="true">
    <polygon points="0,200 404,460 0,460" fill="#eaf8d2"/>
  </svg>
  <div class="green-block"></div>
  <div class="photo" role="img" aria-label="Portrait photo of the advisor, smiling, wearing a teal blouse"></div>

  <div class="name">Carla Vandermeer</div>
  <div class="title">Financial Advisor</div>
  <div class="title-rule"></div>

  <section class="profile">
    <h2>• PROFILE</h2>
    <p>Passionate about helping empower you with knowledge to make informed financial decisions throughout all of life’s stages and help you achieve your goals.</p>
  </section>

  <section class="story">
    <p>• &nbsp;As a business owner, wife, and mother of two teenagers, I understand the struggles you face juggling your personal, business, and financial life.</p>
    <p>• &nbsp;I grew up in a home where my parents had opposing money habits. My Dad was a big spender and mom was a saver. Through the years, I saw how my mom’s consistent savings grew while Dad’s style led to many financial ups and downs. This made a huge impression on me and sparked my continued interest in all things finance.</p>
  </section>

  <div class="top-rule"></div>
  <section class="about">
    <svg class="about-shade" width="372" height="400" viewBox="0 0 372 400" aria-hidden="true">
      <polygon points="0,0 372,270 372,400 0,400" fill="#e6f5d0" opacity=".7"/>
      <polygon points="0,0 30,0 0,12" fill="#dceec4"/>
    </svg>
    <div class="about-text">
      <p>• &nbsp;Having an entrepreneurial personality and ability to explain concepts in a relatable manner has provided me with many opportunities. In 2018, After decades of running a sales agency, I sold my company to spend time with my kids and family but my interest in Finance never waned. Now that our kids are thriving teenagers, I started a new career as a licensed Financial Advisor with a heart to help you achieve your financial dreams.</p>
      <p>• &nbsp;The financial world is changing rapidly, and it can be confusing on how to maneuver through these times. My goal is to pull out the emotions that cloud judgement and help you make better decisions with your long-range goals in mind.</p>
    </div>
  </section>

  <section class="services">
    <h2>Financial planning services offered:</h2>
    <div class="svc"><h3>Transition Planning</h3><ul>
      <li><svg width="10" height="10" viewBox="0 0 10 10"><circle cx="5" cy="5" r="4" fill="none" stroke="#b4e86a" stroke-width="1.2"/><path d="M3 5l1.5 1.5L8 3" fill="none" stroke="#b4e86a" stroke-width="1.2"/></svg>Divorce planning.</li>
      <li><svg width="10" height="10" viewBox="0 0 10 10"><circle cx="5" cy="5" r="4" fill="none" stroke="#b4e86a" stroke-width="1.2"/><path d="M3 5l1.5 1.5L8 3" fill="none" stroke="#b4e86a" stroke-width="1.2"/></svg>Strategy and guidance pre, during, and post- divorce</li>
    </ul></div>
    <div class="svc"><h3>Retirement planning</h3><ul>
      <li><svg width="10" height="10" viewBox="0 0 10 10"><circle cx="5" cy="5" r="4" fill="none" stroke="#b4e86a" stroke-width="1.2"/><path d="M3 5l1.5 1.5L8 3" fill="none" stroke="#b4e86a" stroke-width="1.2"/></svg>Current portfolio analysis</li>
      <li><svg width="10" height="10" viewBox="0 0 10 10"><circle cx="5" cy="5" r="4" fill="none" stroke="#b4e86a" stroke-width="1.2"/><path d="M3 5l1.5 1.5L8 3" fill="none" stroke="#b4e86a" stroke-width="1.2"/></svg>Timeline asset and income planning</li>
      <li><svg width="10" height="10" viewBox="0 0 10 10"><circle cx="5" cy="5" r="4" fill="none" stroke="#b4e86a" stroke-width="1.2"/><path d="M3 5l1.5 1.5L8 3" fill="none" stroke="#b4e86a" stroke-width="1.2"/></svg>Tax and estate review and projections</li>
    </ul></div>
    <div class="svc"><h3>Business sale or purchase:</h3><ul>
      <li><svg width="10" height="10" viewBox="0 0 10 10"><circle cx="5" cy="5" r="4" fill="none" stroke="#b4e86a" stroke-width="1.2"/><path d="M3 5l1.5 1.5L8 3" fill="none" stroke="#b4e86a" stroke-width="1.2"/></svg>Company valuations</li>
      <li><svg width="10" height="10" viewBox="0 0 10 10"><circle cx="5" cy="5" r="4" fill="none" stroke="#b4e86a" stroke-width="1.2"/><path d="M3 5l1.5 1.5L8 3" fill="none" stroke="#b4e86a" stroke-width="1.2"/></svg>Tax impact analysis</li>
      <li><svg width="10" height="10" viewBox="0 0 10 10"><circle cx="5" cy="5" r="4" fill="none" stroke="#b4e86a" stroke-width="1.2"/><path d="M3 5l1.5 1.5L8 3" fill="none" stroke="#b4e86a" stroke-width="1.2"/></svg>Strategy implementation for funds received from sale.</li>
    </ul></div>
    <div class="svc"><h3>Estate planning:</h3><ul>
      <li><svg width="10" height="10" viewBox="0 0 10 10"><circle cx="5" cy="5" r="4" fill="none" stroke="#b4e86a" stroke-width="1.2"/><path d="M3 5l1.5 1.5L8 3" fill="none" stroke="#b4e86a" stroke-width="1.2"/></svg>Strategies for creating future generational wealth.</li>
    </ul></div>
    <div class="svc"><h3>New Investors:</h3><ul>
      <li><svg width="10" height="10" viewBox="0 0 10 10"><circle cx="5" cy="5" r="4" fill="none" stroke="#b4e86a" stroke-width="1.2"/><path d="M3 5l1.5 1.5L8 3" fill="none" stroke="#b4e86a" stroke-width="1.2"/></svg>Assistance in opening investment and retirement acc.</li>
    </ul></div>
    <div class="cta">CALL FOR AN APPOINTMENT</div>
    <div class="phone">
      <span class="phone-icon"><svg width="16" height="16" viewBox="0 0 16 16"><circle cx="8" cy="8" r="7" fill="none" stroke="#2f5b1e" stroke-width="1.2"/><path d="M5.5 4.5l1.3 1.6-.7 1c.5 1 1.3 1.8 2.3 2.3l1-.7 1.6 1.3-.9 1.2C7.6 11 5 8.4 4.3 5.4z" fill="#2f5b1e"/></svg></span>
      555-014-2287
    </div>
    <div class="web">
      <svg width="15" height="15" viewBox="0 0 16 16" fill="none" stroke="#b4e86a" stroke-width="1.2"><circle cx="8" cy="8" r="7"/><ellipse cx="8" cy="8" rx="3" ry="7"/><path d="M1 8h14M2 4.5h12M2 11.5h12"/></svg>
      <span>www.<b>cobaltraadvisors</b>.com</span>
    </div>
  </section>

  <footer class="footer">
    <svg width="12" height="9" viewBox="0 0 12 9"><rect x=".5" y=".5" width="11" height="8" fill="#fff"/><path d="M.5 .5L6 5l5.5-4.5" fill="none" stroke="#2a5219" stroke-width="1"/></svg>
    carla.vandermeer@cobaltraadvisors.com
  </footer>
</div>
</body>
</html>
```